Tralven Networks co-marketing flier

We want a flier that our partners (IT consultants) can hand out to their clients and that we can send to local businesses on their behalf to demonstrate that they can help customers purchase a phone system that has professional features that they would expect in a phone solution that costs thousands of dollars.

We want the brochure to look very professional with excellent layout and use of space.

The Tralven Networks corporate colour is green and more details can be found at www.tralvennetworks-example.com.au.

We have attached a draft Word document that contains most of the information we need but please present the information in the way YOU believe it should be laid out.

We are looking for a designer who understands the concept and uses their own skills to produce a work of art.

Target Market(s)

small businesses that want to save money but also want a modern phone with lots of features

Industry/Entity Type

Marketing

Requirements
Must have
• Must have an image of the main phone and a cordless handset to indicate that they don't need wires to set the system up.

Must have our logo and website address

Must have a box or some "placeholder" where our partners can stamp or insert their details.

Must have a "call to action" saying "Contact us for a quote"

```html
<!DOCTYPE html>
<html lang="en">
<head>
<meta charset="utf-8">
<title>Tralven Networks – Phone System Flier</title>
<link rel="stylesheet" href="https://fonts.googleapis.com/css2?family=Oswald:wght@500;600&family=Open+Sans:wght@400;600&family=Arimo:wght@700&family=Cormorant+Garamond:ital,wght@1,500&display=swap">
<style>
  :root {
    --green: #2e8b2e;
    --green-dark: #1f6e1f;
    --green-light: #5cc24a;
    --blue: #1d5d93;
    --blue-dark: #0f3a66;
    --blue-light: #4a9ad6;
    --ink: #333;
    --muted: #555;
    --bg-light: #ffffff;
    --bg-grey: #c9c9c9;
    --panel-border: #8a8a8a;
  }
  * { margin: 0; padding: 0; box-sizing: border-box; }
  html, body { width: 849px; height: 1200px; overflow: hidden; }
  body {
    position: relative;
    background: radial-gradient(ellipse at 60% 45%, var(--bg-light) 0%, #efefef 40%, var(--bg-grey) 100%);
    font-family: "Open Sans", Arial, sans-serif;
    color: var(--ink);
  }
  .abs { position: absolute; }
  .product-photo { border-radius: 24px; }
  .handset-photo { left: 70px; top: 22px; width: 145px; height: 305px;
    background: linear-gradient(180deg, #2a2a2a, #111 70%, #3a3a3a); border-radius: 40px 40px 20px 20px; }
  .desk-photo { left: 285px; top: 36px; width: 515px; height: 335px;
    background: linear-gradient(160deg, #e6e6e6 0%, #b9b9b9 45%, #2a2a2a 100%); border-radius: 30px; }
  .connectors { left: 0; top: 0; }
  .bubble-label {
    position: absolute; color: #fff; text-align: center; text-transform: uppercase;
    text-shadow: 0 1px 2px rgba(0,0,0,.4); font-weight: 700;
  }
  .hero-label { left: 222px; top: 356px; width: 196px; font-family: "Oswald", sans-serif;
    font-weight: 600; font-size: 26px; line-height: 32px; }
  .why-label { left: 20px; top: 556px; width: 136px; font-family: "Arimo", sans-serif; font-size: 19px; }
  .features-label { left: 412px; top: 527px; width: 136px; font-family: "Arimo", sans-serif; font-size: 20px; }
  .contact-label { left: 80px; top: 1013px; width: 154px; font-family: "Arimo", sans-serif; font-size: 18px; line-height: 26px; }
  .panel { background: var(--green); border-radius: 8px; color: #fff; }
  .why-panel { left: 123px; top: 590px; width: 289px; height: 284px; }
  .why-panel p { position: absolute; left: 20px; top: 38px; width: 249px; text-align: center;
    font-family: "Arimo", sans-serif; font-weight: 700; font-size: 13.5px; line-height: 18px; }
  .tagline { position: absolute; left: 0; top: 170px; width: 100%; text-align: center;
    font-family: "Cormorant Garamond", serif; font-style: italic; font-weight: 500;
    font-size: 34px; line-height: 35px; letter-spacing: 1.5px; }
  .tagline strong { font-family: "Arimo", sans-serif; font-style: normal; font-weight: 700;
    font-size: 29px; letter-spacing: 0; }
  .features-intro { left: 555px; top: 568px; font-size: 16px; color: var(--muted); }
  .features-panel { left: 492px; top: 590px; width: 313px; height: 284px; }
  .feature-list { list-style: none; position: absolute; left: 32px; top: 28px; width: 250px;
    font-size: 14.5px; line-height: 20px; }
  .feature-list li { position: relative; padding-left: 29px; margin-bottom: 6px; }
  .feature-list li::before { content: "+"; position: absolute; left: 0; top: -6px;
    font-family: "Arimo", sans-serif; font-weight: 700; font-size: 26px; }
  .icon-tab { border-radius: 3px; display: flex; align-items: center; justify-content: center; color: #fff; font-weight: 600; }
  .brand-name { left: 248px; top: 1004px; font-size: 25px; line-height: 32px; font-weight: 600; color: var(--green); }
  .company-details { left: 248px; top: 1042px; width: 236px; color: var(--ink); }
  .company-details .entity { font-size: 13.5px; line-height: 18px; }
  .company-details .abn { font-size: 12px; line-height: 16px; }
  .company-details .web { font-size: 13px; line-height: 18px; }
  .partner-stamp { left: 491px; top: 978px; width: 315px; height: 115px; background: #fff;
    border: 2px solid var(--panel-border); border-radius: 10px; }
</style>
</head>
<body>
  <div class="abs product-photo handset-photo" role="img" aria-label="Photo of a black cordless handset in its charging cradle"></div>
  <div class="abs product-photo desk-photo" role="img" aria-label="Photo of a silver and black desk phone with colour screen and corded receiver"></div>

  <svg class="abs connectors" width="849" height="1200" viewBox="0 0 849 1200" aria-hidden="true">
    <defs>
      <radialGradient id="greenOrb" cx="45%" cy="35%" r="70%">
        <stop offset="0" stop-color="#7fd86a"/><stop offset=".55" stop-color="#2f9a2f"/><stop offset="1" stop-color="#145d14"/>
      </radialGradient>
      <radialGradient id="blueOrb" cx="45%" cy="35%" r="70%">
        <stop offset="0" stop-color="#6fb3e6"/><stop offset=".55" stop-color="#1d5d93"/><stop offset="1" stop-color="#0b2f55"/>
      </radialGradient>
    </defs>
    <g fill="none" stroke="#2e8b2e" stroke-width="2">
      <path d="M220 398 H90 V500"/>
      <path d="M155 540 H412"/>
      <path d="M483 600 V918 H160 V968"/>
    </g>
    <g fill="none" stroke="#2e8b2e" stroke-width="4">
      <path d="M80 432 l9 9 l9 -9 M80 444 l9 9 l9 -9"/>
      <path d="M290 531 l9 9 l-9 9 M302 531 l9 9 l-9 9"/>
      <path d="M315 909 l-9 9 l9 9 M303 909 l-9 9 l9 9"/>
    </g>
    <circle cx="320" cy="410" r="104" fill="#fff" stroke="#ddd"/>
    <circle cx="320" cy="410" r="97" fill="url(#blueOrb)"/>
    <circle cx="88" cy="570" r="74" fill="#fff" stroke="#ddd"/>
    <circle cx="88" cy="570" r="68" fill="url(#greenOrb)"/>
    <circle cx="480" cy="540" r="72" fill="#fff" stroke="#ddd"/>
    <circle cx="480" cy="540" r="66" fill="url(#greenOrb)"/>
    <circle cx="155" cy="1040" r="80" fill="#fff" stroke="#ddd"/>
    <circle cx="155" cy="1040" r="74" fill="url(#greenOrb)"/>
  </svg>

  <div class="abs icon-tab" style="left:418px;top:374px;width:58px;height:52px;background:var(--blue);">
    <svg width="30" height="30" viewBox="0 0 24 24" aria-hidden="true"><path fill="#fff" d="M6.6 10.8a15 15 0 0 0 6.6 6.6l2.2-2.2c.3-.3.7-.4 1-.2 1.1.4 2.300.6 3.6.6.6 0 1 .4 1 1V20c0 .6-.4 1-1 1A17 17 0 0 1 3 4c0-.6.4-1 1-1h3.5c.6 0 1 .4 1 1 0 1.3.2 2.5.6 3.6.1.3 0 .7-.2 1z"/></svg>
  </div>
  <div class="abs icon-tab" style="left:160px;top:552px;width:40px;height:34px;background:var(--green);font-size:24px;">?</div>
  <div class="abs icon-tab" style="left:548px;top:522px;width:40px;height:36px;background:var(--green);font-size:30px;">+</div>
  <div class="abs icon-tab" style="left:37px;top:1020px;width:44px;height:40px;background:var(--green);font-size:26px;">@</div>

  <div class="bubble-label hero-label">Looking for<br>a new phone<br>system?</div>
  <div class="bubble-label why-label">Why us?</div>
  <div class="bubble-label features-label">Features</div>
  <div class="bubble-label contact-label">Contact us<br>for a quote</div>

  <section class="abs panel why-panel">
    <p>Our proven VoIP solution comes<br>with all the professional features to<br>service an office of up to 6 people.</p>
    <div class="tagline">It’s <strong>cheaper</strong><br>than you think.</div>
  </section>

  <div class="abs features-intro">includes, but not limited to:</div>
  <section class="abs panel features-panel">
    <ul class="feature-list">
      <li>very low line rental rates*</li>
      <li>10c local and national calls untimed</li>
      <li>voicemail-to-email</li>
      <li>direct in-dial to every extension</li>
      <li>number portability (keep your number when you move)</li>
      <li>call records via spreadsheet</li>
      <li>flat rate local and national calls</li>
    </ul>
  </section>

  <div class="abs brand-name">Tralven Networks</div>
  <div class="abs company-details">
    <div class="entity">kestrow (Marlow Group Pty Ltd)</div>
    <div class="abn">ABN: 12 345 678 901</div>
    <div class="web">www.tralvennetworks-example.com.au</div>
  </div>

  <div class="abs partner-stamp" aria-label="Space for partner details"></div>
</body>
</html>
```